Korelith InsurTech Website Redesign - 10 Pages

Design a modern, professional website for Korelith, an AI-native cyber insurance platform serving SMBs.

DELIVERABLE: 10 pages (desktop + mobile mockups)
- Homepage (priority #1)
- 4 Platform pages (Cyber Insurance, Brokers, Underwriters, Policyholder)
- 3 Company pages (About Us, Team, Contact/Careers)
- 2 Risk pages (AI Risk, Cyber Risk)

DESIGN DIRECTION:
- Professional + innovative (insurance meets technology)
- Trust-building + modern aesthetic
- Reference: Brambury Insurance, Tidewick Insurance
- Use official brand colors (6-color palette provided)
- Avoid generic security clipart (padlocks, shields, magnifying glasses)
- Custom graphics, not AI-generated or stock imagery

CURRENT SITES FOR REFERENCE:
- www.korelith.ai
- https://a3c9124d.korelith-website.vorlapages.dev/

Full detailed brief with all content, page specifications, and brand guidelines attached as PDF (Korelith_PixelHarbor_Brief.pdf).

TARGET AUDIENCE: Insurance brokers (primary), SMB business owners (secondary)
KEY MESSAGE: "Cyber Insurance the Way It Should Be"

Additional brand assets available in Google Drive - link provided on request.

```html
<!DOCTYPE html>
<html lang="en">
<head>
<meta charset="utf-8">
<title>Korelith – Contact Us</title>
<link rel="stylesheet" href="https://fonts.googleapis.com/css2?family=Oxygen:wght@400;700&family=Lato:wght@400&family=Noto+Serif:wght@700&display=swap">
<style>
:root{
  --brand:#1a12b8;
  --ink:#333340;
  --line:#9a9aa6;
  --white:#ffffff;
  --mint-1:#e9fbe7;
  --mint-2:#dcfbd8;
  --teal-1:#62d4c9;
  --teal-2:#4a9db0;
  --base-band:#3333ff;
  --hero-1:#0e2a6e;
  --hero-2:#1d1a9e;
  --hero-glow:#e9c4c8;
}
*{margin:0;padding:0;box-sizing:border-box}
html,body{width:706px;height:1200px;overflow:hidden;background:var(--white)}
body{position:relative;font-family:"Oxygen",sans-serif;color:var(--ink)}
.abs{position:absolute}
.brand-name{font-family:"Oxygen",sans-serif;font-weight:700;color:var(--brand);display:flex;align-items:center;gap:6px;white-space:nowrap}
.brand-mark{width:12px;height:12px;border-radius:50%;background:var(--brand)}
.site-header{left:0;top:0;width:706px;height:98px}
.nav-panel{left:0;top:0}
.header-brand{left:121px;top:22px;font-size:20px}
.nav-link{top:26px;font-size:11.5px;color:var(--ink);display:flex;align-items:center;gap:4px}
.nav-link.is-active{color:var(--brand);font-weight:700}
.hero{left:0;top:98px;width:706px;height:248px;
  background:radial-gradient(ellipse 90px 70px at 354px 135px,var(--hero-glow) 0%,rgba(120,110,220,.6) 45%,transparent 100%),
  linear-gradient(100deg,var(--hero-1) 0%,#1f4a9a 40%,var(--hero-2) 100%)}
.hero-title{left:0;top:212px;width:706px;text-align:center;color:var(--white);font-weight:700;font-size:19px;letter-spacing:.5px}
.decor{left:0;top:0}
.section-title{top:390px;font-size:17px;font-weight:700;color:var(--brand);letter-spacing:.3px}
.field-label{font-size:10.5px;color:var(--ink)}
.field-label .req{font-size:8px;vertical-align:top;margin-left:3px}
.field{background:var(--white);border:1px solid var(--line);border-radius:3px}
.submit{left:108px;top:839px;width:71px;height:24px;background:var(--brand);color:var(--white);border:0;border-radius:3px;
  font-family:"Noto Serif",serif;font-weight:700;font-size:9px;display:flex;align-items:center;justify-content:center}
.site-footer{left:0;top:908px;width:706px;height:260px;background:linear-gradient(100deg,var(--teal-1) 0%,#55bdbd 55%,var(--teal-2) 100%)}
.footer-brand{left:112px;top:988px;font-size:20px}
.footer-tagline{left:108px;top:1031px;width:130px;font-family:"Lato",sans-serif;font-size:7.3px;line-height:16px;color:var(--white)}
.footer-col{list-style:none;font-size:8px;color:var(--white)}
.footer-col li{height:16px;line-height:16px}
.footer-col .col-head{font-weight:700}
.base-band{left:0;top:1168px;width:706px;height:32px;background:var(--base-band)}
</style>
</head>
<body>

<svg class="abs decor" width="706" height="1200" aria-hidden="true">
  <polygon points="577,470 706,470 706,595 674,651 483,651" fill="var(--mint-1)"/>
  <path d="M482 683 H706 V907 H686 C686 870 668 848 630 848 H577 Z" fill="var(--mint-2)"/>
</svg>

<header class="abs site-header">
  <svg class="abs nav-panel" width="706" height="98" aria-hidden="true">
    <defs>
      <linearGradient id="navShade" x1="0" y1="0" x2="0" y2="1">
        <stop offset="0" stop-color="#000" stop-opacity=".12"/>
        <stop offset="1" stop-color="#000" stop-opacity="0"/>
      </linearGradient>
    </defs>
    <polygon points="182,71 706,71 706,84 206,84" fill="url(#navShade)"/>
    <polygon points="179,0 706,0 706,71 220,71" fill="var(--white)"/>
    <line x1="179" y1="0" x2="220" y2="71" stroke="#e2e2e6" stroke-width="1"/>
  </svg>
  <div class="abs brand-name header-brand"><span class="brand-mark"></span>korelith</div>
  <nav>
    <a class="abs nav-link" style="left:222px">Home</a>
    <a class="abs nav-link" style="left:292px">Platform
      <svg width="8" height="6" viewBox="0 0 8 6"><path d="M1 1.5 L4 4.5 L7 1.5" fill="none" stroke="currentColor" stroke-width="1.3"/></svg></a>
    <a class="abs nav-link" style="left:376px">Cyber Risk</a>
    <a class="abs nav-link" style="left:470px">AI Risk</a>
    <a class="abs nav-link is-active" style="left:546px">Company
      <svg width="8" height="6" viewBox="0 0 8 6"><path d="M1 1.5 L4 4.5 L7 1.5" fill="none" stroke="currentColor" stroke-width="1.3"/></svg></a>
  </nav>
</header>

<section class="abs hero" role="img" aria-label="Futuristic digital scene with a glowing orb above a circular holographic platform in deep blue tones"></section>
<h1 class="abs hero-title">Contact Us</h1>

<main>
  <h2 class="abs section-title" style="left:108px">Send a Message</h2>
  <h2 class="abs section-title" style="left:359px">Call-to-action</h2>

  <form>
    <label class="abs field-label" style="left:109px;top:432px">Name<span class="req">*</span></label>
    <div class="abs field" style="left:109px;top:453px;width:236px;height:36px"></div>
    <label class="abs field-label" style="left:109px;top:499px">Email<span class="req">*</span></label>
    <div class="abs field" style="left:109px;top:520px;width:236px;height:36px"></div>
    <label class="abs field-label" style="left:109px;top:566px">Company</label>
    <div class="abs field" style="left:109px;top:587px;width:236px;height:36px"></div>
    <label class="abs field-label" style="left:109px;top:633px">Message</label>
    <div class="abs field" style="left:109px;top:654px;width:238px;height:158px"></div>
    <div class="abs submit">Submit</div>
  </form>

  <div>
    <label class="abs field-label" style="left:360px;top:432px">Email<span class="req">*</span></label>
    <div class="abs field" style="left:360px;top:453px;width:237px;height:36px"></div>
    <label class="abs field-label" style="left:360px;top:499px">Office<span class="req">*</span></label>
    <div class="abs field" style="left:360px;top:520px;width:237px;height:36px"></div>
    <p class="abs field-label" style="left:360px;top:571px">Follow Us</p>
    <p class="abs field-label" style="left:360px;top:592px">Linkora</p>
  </div>
</main>

<footer>
  <div class="abs site-footer" role="img" aria-label="Teal-tinted aerial view of a glowing digital city"></div>
  <div class="abs brand-name footer-brand"><span class="brand-mark"></span>korelith</div>
  <p class="abs footer-tagline">Reducing the frequency and severity of cyber risk by strengthening organizations’ cyber risk posture.</p>
  <ul class="abs footer-col" style="left:275px;top:1029px">
    <li class="col-head">Home</li><li>Platform</li><li>Cyber Risk</li><li>AI Risk</li><li>Company</li>
  </ul>
  <ul class="abs footer-col" style="left:387px;top:1030px">
    <li class="col-head">Company</li><li>The Problem</li><li>The Solution</li><li>How it Works</li>
  </ul>
  <ul class="abs footer-col" style="left:485px;top:1030px">
    <li class="col-head">Other</li><li>Privacy Policy</li><li>Terms and Conditions</li>
  </ul>
  <div class="abs base-band"></div>
</footer>

</body>
</html>
```